Truck Wrap for Desk Depot Outlet

We need a professionally designed truck wrap for our 26' box delivery trucks. DDO is a leading provider of new and used office furniture, workspace solutions, and architectural walls in South Florida. We have been in business 35 years. We would like to see designs with a red background on our truck wrap. Our logo is a simple stencil font. The final design should be clean an eye catching.

Target Market(s)

Businesses of all sizes

Industry/Entity Type

Commercial Office Furniture

Font styles to use
Other font styles liked:
• Stencil font for the company logo

Colors

Designer to choose colors to be used in the design.

Requirements
Must have
• Red background CMYK: 0, 90, 91, 6
Should not have
• I don't want the words overly crowded. It must be easy to read.

```html
<!DOCTYPE html>
<html lang="en">
<head>
<meta charset="utf-8">
<title>Desk Depot Outlet – Truck Wrap Panels</title>
<link rel="stylesheet" href="https://fonts.googleapis.com/css2?family=Rubik:wght@800&family=Open+Sans:wght@400;600;700&display=swap">
<style>
  :root{
    --brand-red:#ef1816;
    --deep-red:#8c0a0c;
    --ink:#0d0d0d;
    --paper:#ffffff;
    --photo-tone:#d9d3c8;
    --stage:#2a2d3b;
    --head-font:"Rubik", Arial, sans-serif;
    --body-font:"Open Sans", Arial, sans-serif;
  }
  *{box-sizing:border-box;margin:0;padding:0}
  html,body{width:1200px;height:2700px;overflow:hidden}
  body{background:var(--stage);position:relative;font-family:var(--body-font)}

  .panel{position:absolute;background:var(--brand-red);overflow:hidden}

  /* brand name block */
  .brand{position:absolute;color:var(--paper);text-align:center}
  .brand .name{font-family:var(--head-font);font-weight:800;line-height:1;white-space:nowrap}
  .brand .tagline{font-family:var(--body-font);font-weight:400;margin-top:8px;white-space:nowrap}

  /* front header */
  .front{left:390px;top:60px;width:420px;height:130px}
  .front .brand{left:0;top:34px;width:420px}
  .front .name{font-size:30px}
  .front .tagline{font-size:12px}

  /* side panels */
  .side{left:100px;width:1000px;height:330px}
  .side-left{top:820px}
  .side-right{top:2110px}
  .side .swoosh{position:absolute;inset:0;width:1000px;height:330px}
  .side .brand{top:52px;width:520px}
  .side .name{font-size:42px}
  .side .tagline{font-size:14px}
  .phone-band{position:absolute;top:160px;height:62px;background:var(--ink);display:flex;justify-content:space-around;align-items:center}
  .phone{text-align:center}
  .phone .area{display:block;color:var(--brand-red);font-size:12px;line-height:1.1}
  .phone .number{display:block;color:var(--paper);font-weight:700;font-size:24px;letter-spacing:.5px}
  .benefits{position:absolute;top:238px;color:var(--paper);font-size:12px;font-weight:600;text-align:center}
  .benefits .sep{opacity:.7;margin:0 4px}
  .offer-head{position:absolute;top:16px;width:250px;text-align:center;font-family:var(--head-font);font-weight:800;font-size:23px;line-height:1.02;color:var(--brand-red)}
  .photo{position:absolute;background:linear-gradient(180deg,#f4f4f4 0%,var(--photo-tone) 100%);border-radius:4px}
  .url-pill{position:absolute;background:var(--deep-red);color:var(--paper);font-family:var(--head-font);font-weight:800;font-size:14px;letter-spacing:1px;border-radius:18px;text-align:center;line-height:34px}
  .trim{position:absolute;left:0;right:0;bottom:4px;height:5px;background:repeating-linear-gradient(90deg,var(--brand-red) 0 40px,transparent 40px 60px)}

  .side-left .brand{left:40px}
  .side-left .phone-band{left:0;width:600px}
  .side-left .benefits{left:0;width:600px}
  .side-left .offer-head{left:738px}
  .side-left .photo{left:742px;top:82px;width:242px;height:150px}
  .side-left .url-pill{left:793px;top:256px;width:150px}

  .side-right .swoosh{transform:scaleX(-1)}
  .side-right .brand{left:440px}
  .side-right .phone-band{left:400px;width:600px}
  .side-right .benefits{left:400px;width:600px}
  .side-right .offer-head{left:12px}
  .side-right .photo{left:16px;top:82px;width:242px;height:150px}
  .side-right .url-pill{left:57px;top:256px;width:150px}

  /* rear door */
  .rear{left:370px;top:1390px;width:460px;height:460px;background:var(--paper)}
  .rear .red-field{position:absolute;left:0;top:0;width:460px;height:262px;background:var(--brand-red)}
  .rear .brand{left:0;top:60px;width:460px}
  .rear .name{font-size:38px}
  .rear .tagline{font-size:14px}
  .rear .offer-head{left:0;top:178px;width:460px;font-size:21px;color:var(--ink)}
  .rear .range{position:absolute;left:0;top:222px;width:460px;text-align:center;color:var(--paper);font-size:11px;font-weight:600}
  .rear .phone-band{left:0;top:262px;width:460px;height:62px}
  .rear .url-tab{position:absolute;left:148px;top:324px;width:168px;height:26px;background:var(--deep-red);color:var(--paper);font-family:var(--head-font);font-weight:800;font-size:14px;letter-spacing:1px;text-align:center;line-height:26px;clip-path:polygon(0 0,100% 0,94% 100%,6% 100%)}
  .rear .photo{left:14px;top:358px;width:432px;height:92px}
</style>
</head>
<body>

  <!-- front header panel -->
  <section class="panel front" aria-label="Front header panel">
    <div class="brand">
      <div class="name">DESK DEPOT OUTLET</div>
      <div class="tagline">Furnishing South Florida since 1990</div>
    </div>
  </section>

  <!-- driver side panel -->
  <section class="panel side side-left" aria-label="Driver side panel">
    <div class="phone-band">
      <div class="phone"><span class="area">Broward/palm Beach</span><span class="number">954-555-0147</span></div>
      <div class="phone"><span class="area">Miami Dade</span><span class="number">305-555-0182</span></div>
    </div>
    <svg class="swoosh" viewBox="0 0 1000 330" aria-hidden="true">
      <defs>
        <linearGradient id="swooshL" x1="0" y1="0" x2="1" y2="1">
          <stop offset="0" stop-color="#6e0608"/><stop offset="1" stop-color="#d4121a"/>
        </linearGradient>
      </defs>
      <path d="M625,0 L700,0 C690,200 790,300 960,330 L830,330 C660,300 600,170 625,0Z" fill="url(#swooshL)"/>
      <path d="M700,0 L1000,0 L1000,330 L960,330 C790,300 690,200 700,0Z" fill="#ffffff"/>
    </svg>
    <div class="brand">
      <div class="name">DESK DEPOT OUTLET</div>
      <div class="tagline">Furnishing South Florida since 1990</div>
    </div>
    <div class="benefits">Huge Selection<span class="sep">|</span>Everyday Low Prices<span class="sep">|</span>Quick Profesional Delivery</div>
    <div class="offer-head">New &amp; Used Office Furniture</div>
    <div class="photo" role="img" aria-label="Photo of a wooden conference table with white office chairs"></div>
    <div class="url-pill">WWW.DDOFL.COM</div>
    <div class="trim"></div>
  </section>

  <!-- rear door panel -->
  <section class="panel rear" aria-label="Rear door panel">
    <div class="red-field"></div>
    <div class="brand">
      <div class="name">DESK DEPOT OUTLET</div>
      <div class="tagline">Furnishing South Florida since 1990</div>
    </div>
    <div class="offer-head">New &amp; Used Office Furniture</div>
    <div class="range">Desks | Chairs | Tables | Cubicles | Files | Workstations | Architectural | Walls</div>
    <div class="phone-band">
      <div class="phone"><span class="area">Broward/palm Beach</span><span class="number">954-555-0147</span></div>
      <div class="phone"><span class="area">Miami Dade</span><span class="number">305-555-0182</span></div>
    </div>
    <div class="url-tab">WWW.DDOFL.COM</div>
    <div class="photo" role="img" aria-label="Photo of a conference table with chairs and a white cubicle workstation"></div>
  </section>

  <!-- passenger side panel -->
  <section class="panel side side-right" aria-label="Passenger side panel">
    <div class="phone-band">
      <div class="phone"><span class="area">Miami Dade</span><span class="number">305-555-0182</span></div>
      <div class="phone"><span class="area">Broward/palm Beach</span><span class="number">954-555-0147</span></div>
    </div>
    <svg class="swoosh" viewBox="0 0 1000 330" aria-hidden="true">
      <defs>
        <linearGradient id="swooshR" x1="0" y1="0" x2="1" y2="1">
          <stop offset="0" stop-color="#6e0608"/><stop offset="1" stop-color="#d4121a"/>
        </linearGradient>
      </defs>
      <path d="M625,0 L700,0 C690,200 790,300 960,330 L830,330 C660,300 600,170 625,0Z" fill="url(#swooshR)"/>
      <path d="M700,0 L1000,0 L1000,330 L960,330 C790,300 690,200 700,0Z" fill="#ffffff"/>
    </svg>
    <div class="brand">
      <div class="name">DESK DEPOT OUTLET</div>
      <div class="tagline">Furnishing South Florida since 1990</div>
    </div>
    <div class="benefits">Huge Selection<span class="sep">|</span>Everyday Low Prices<span class="sep">|</span>Quick Profesional Delivery</div>
    <div class="offer-head">New &amp; Used Office Furniture</div>
    <div class="photo" role="img" aria-label="Photo of a wooden conference table with white office chairs"></div>
    <div class="url-pill">WWW.DDOFL.COM</div>
    <div class="trim"></div>
  </section>

</body>
</html>
```